Thank you for exploring whether you are interested in creating a book cover for the Insight Lantern!

The cover should look professional yet appeal to a person who is open to approaching life more deeply.

The logo that I've uploaded is something that you are welcome to use in your book cover design but is not required to be the primary graphic.

The following is a description of the Insight Lantern and its purpose.
RADICAL CLARITY IS POSSIBLE

Are you tired of hitting up against your limitations? Do you wish you could be more effective in everything you do? What would it be like if you could walk confidently into any situation and automatically comprehend it, organize your thoughts, and respond creatively? This kind of radical clarity is not only possible, it’s right in front of you—and The Insight Lantern: Notice What Matters. Hold Bold Dialogues. Build the Days You Crave. shows you the pathway to get there!

In the book, Dr. Lorne Haskett draws on over 30 years of experience with executive coaching and leadership development to deliver priceless wisdom about how to see clearly in today’s complex and uncertain world. Using his Insight Lantern, you’ll discover where you’re stuck and why, find your authentic direction, and learn to engage creatively with life so you can start getting what you really want.

A TRANSFORMATIONAL TOOL

The Insight Lantern is a cutting-edge leadership development tool that supports you to activate your maximum potential, both personally and professionally. It’s based on the idea that there are four fundamental building blocks to reality: Intentions, Actions, Facts, and Stories. Understanding the differences between these dimensions of your experience and learning how they work together is the key to forging a clear path toward your destination in life. The Insight Lantern organizes these four main building blocks around the two polarities of a compass:

1. North to South – Intentions to Actions
We all have billions of intentions, but how many do we actually put into action? In this polarity you learn to notice and implement your intentions in order to generate more effective actions and create meaningful outcomes in your life.

2. East vs. West – Facts vs. Stories
We all create stories to make sense of life, but how many of us actually get clear on the facts to see where our stories might be off? In this polarity you learn to discern the objective facts from your subjective interpretations and stories, illuminating a clearer perspective to uncover what’s been blocking you on the path to success.

Using the Insight Lantern you’ll discover how naming and implementing your intentions in life naturally results in more effective behavior and actions, and how distinguishing the real facts from your interpretations of any situation can propel you toward radical clarity and true fulfillment.

BOLD DIALOGUES

The key benefit of using the Insight Lantern is that you’ll have more of what Lorne calls “Bold Dialogues.” Bold dialogues are those that move you closer to what you’re wanting in life—the kind of human-to-human interactions that actually make a difference. By applying the Insight Lantern, you gain critical insight that opens your eyes to new opportunities for Bold Dialogues, helping you draw on your imagination and move beyond your current stance toward a positive outcome. Every conversation is a possibility waiting to be discovered. The more Bold Dialogues you have, the more profound and meaningful shifts you activate in your life.

PRACTICAL GUIDANCE

The book doesn’t just give you a theoretical understanding of how to gain more clarity in your life. Dr. Haskett provides you with clear, practical steps to develop the core competencies you need to start getting the results you want. As you explore the book, you’ll find:

• A thorough description of all the directions of the Insight Lantern, each with three main points to focus your energy on.
• Case studies from Lorne’s many clients who have successfully used the Insight Lantern to transform their own lives.
• Hands-on practices Lorne has developed to help you put your new skills to use immediately.
• Step-by-step guidance to apply the Insight Lantern in any situation, including real-life stories from people who have experienced genuine transformation using this tool.

The Insight Lantern will help you to deepen your understanding of the challenges in your life, integrate new competencies to boost your effectiveness, and awaken to exciting opportunities for your own growth, leadership, and success!

ABOUT THE AUTHOR

Dr. Lorne Haskett has over 30 years of experience with leadership development and executive coaching work. As owner and principal coach of Haskett Leadership Consultants, he has been integrating the fields of management consulting, business psychology, and leadership coaching since 1983. Lorne holds a Ph.D. in psychodynamic and group psychology from the Merrowind Graduate Institute, an M.A. in human growth and potential from the University of Fallbrook Ridge, and a B.A. in accounting and Business Administration from Kestrel Vale University. He is the creator of the Insight Lantern™, a leadership development tool that supports people to see life clearly, wake up to exciting opportunities for their own growth and leadership, and take empowered action toward true success. Lorne’s combination of business expertise, human compassion, and incisive questions help his clients achieve unprecedented results.

Target Market(s)

Out intended audience is folks who would like to be more effective and to grow and transform. This being more productive and developing could be in their careers or their personal lives.

Industry/Entity Type

It Professional

Requirements
Must have
• Stock images, if used, that I can purchase exclusively or that you can easily create specifically for the book once you are the chosen designer. I completely understand using stock imaging in your submissions pre-selection.
Nice to have
• Ideally the cover will include both the title and subtitle.

```html
<!DOCTYPE html>
<html lang="en">
<head>
<meta charset="utf-8">
<title>The Insight Lantern — Book Cover</title>
<link href="https://fonts.googleapis.com/css2?family=Jost:wght@400;500&family=Libre+Baskerville:ital,wght@0,700;1,400&display=swap" rel="stylesheet">
<style>
  :root {
    --page-bg: #f4f4f4;
    --sky-top: #2f3f7a;
    --sky-upper: #3d4a86;
    --sky-mid: #7a5f8c;
    --sky-glow: #e9a36a;
    --sky-warm: #e4763f;
    --sky-low: #b8553a;
    --sky-base: #6e4a52;
    --ink-light: #ffffff;
    --ink-soft: #f3ece6;
  }
  html, body {
    margin: 0;
    width: 1200px;
    height: 1200px;
    overflow: hidden;
    background: var(--page-bg);
  }
  .stage {
    width: 1200px;
    height: 1200px;
    display: flex;
    align-items: center;
    justify-content: center;
  }
  .cover {
    position: relative;
    width: 740px;
    height: 1110px;
    overflow: hidden;
    box-shadow: 0 6px 24px rgba(0,0,0,0.18);
  }
  .cover-art {
    position: absolute;
    inset: 0;
    background: linear-gradient(180deg,
      var(--sky-top) 0%,
      var(--sky-upper) 28%,
      var(--sky-mid) 46%,
      var(--sky-glow) 62%,
      var(--sky-warm) 74%,
      var(--sky-low) 86%,
      var(--sky-base) 100%);
  }
  .title {
    position: absolute;
    top: 70px;
    left: 0;
    right: 0;
    margin: 0;
    font-family: "Jost", sans-serif;
    font-weight: 400;
    color: var(--ink-light);
    text-align: center;
    line-height: 1;
  }
  .title-top {
    display: block;
    font-size: 118px;
    letter-spacing: -1px;
  }
  .title-main {
    display: flex;
    align-items: center;
    justify-content: center;
    gap: 18px;
    margin-top: 6px;
    font-size: 112px;
    letter-spacing: 1px;
  }
  .title-mark {
    width: 26px;
    height: 26px;
    border-radius: 50%;
    background: var(--ink-light);
  }
  .subtitle {
    position: absolute;
    top: 330px;
    left: 0;
    right: 0;
    margin: 0;
    font-family: "Jost", sans-serif;
    font-weight: 400;
    font-size: 27px;
    letter-spacing: 2px;
    color: var(--ink-light);
    text-align: center;
    line-height: 1.25;
    text-transform: uppercase;
  }
  .credit {
    position: absolute;
    top: 870px;
    left: 0;
    right: 0;
    text-align: center;
    font-family: "Libre Baskerville", serif;
    color: var(--ink-soft);
  }
  .credit-label {
    display: block;
    font-weight: 700;
    font-size: 24px;
    letter-spacing: 1px;
  }
  .credit-name {
    display: block;
    margin-top: 6px;
    font-style: italic;
    font-size: 30px;
  }
</style>
</head>
<body>
  <main class="stage">
    <article class="cover">
      <div class="cover-art" role="img" aria-label="Photograph of a hang glider soaring through a twilight sky over glowing orange clouds and snowy mountains, with the sun low on the right"></div>
      <h1 class="title">
        <span class="title-top">The Insight</span>
        <span class="title-main"><span class="title-mark"></span>LANTERN</span>
      </h1>
      <p class="subtitle">
        Notice What Matters<br>
        Hold Bold Dialogues<br>
        Build the Days You Crave
      </p>
      <p class="credit">
        <span class="credit-label">Edited by</span>
        <span class="credit-name">Dr. Lorne Haskett</span>
      </p>
    </article>
  </main>
</body>
</html>
```